Online-Marketing-Material für Reinigungsunternehmen
Zielgruppe
Wir sind ein seit Jahresanfang bestehende Reinigungsunternehmen.
Unsere Schwerpunkte liegen auf Treppenhausreinigung und Büroreinigung.
Die Anzeige soll auf Facebook / Instagram als Werbung angezeigt werden.
Kunden sind sowohl Unternehmer sowie auch Privathaushalte und Hausverwaltungen.
www.kolvaputz.de
Aufgabenstellung
Es darf gerne Modern und verspielt sein. Es soll und darf nicht billig wirken.
Wir haben auch ein Maskottchen. Es muss aber nicht auf die Anzeige mit drauf!

```html
<!DOCTYPE html>
<html lang="de">
<head>
<meta charset="UTF-8">
<title>Kolva Putz – Anzeige</title>
<link href="https://fonts.googleapis.com/css2?family=Poppins:wght@400;500;600;700;800&display=swap" rel="stylesheet">
<style>
  :root {
    --brand-blue: #2f4f9e;
    --brand-navy: #2e4a9a;
    --brand-green: #6db72e;
    --brand-teal: #41b8a8;
    --sky: #4f8fd9;
    --white: #ffffff;
  }
  html, body {
    margin: 0;
    padding: 0;
    width: 1200px;
    height: 1200px;
    overflow: hidden;
    background: var(--white);
  }
  .ad {
    position: relative;
    width: 1200px;
    height: 1200px;
    overflow: hidden;
    font-family: "Poppins", sans-serif;
    color: var(--white);
  }
  .ad__backdrop {
    position: absolute;
    inset: 0;
    width: 1200px;
    height: 1200px;
  }
  .brand {
    position: absolute;
    left: 550px;
    top: 100px;
    display: flex;
    align-items: center;
    gap: 28px;
  }
  .brand__square {
    width: 200px;
    height: 200px;
    background: var(--brand-blue);
    border-radius: 6px;
  }
  .brand__text {
    display: flex;
    flex-direction: column;
  }
  .brand__name {
    font-weight: 700;
    font-size: 64px;
    line-height: 0.98;
    color: var(--brand-blue);
    letter-spacing: -1px;
  }
  .brand__owner {
    margin-top: 12px;
    font-weight: 400;
    font-size: 23px;
    color: var(--brand-teal);
  }
  .headline {
    margin: 0;
    font-weight: 700;
    text-transform: uppercase;
  }
  .headline__lead {
    position: absolute;
    left: 99px;
    top: 695px;
    font-size: 70px;
    line-height: 1;
    letter-spacing: -0.5px;
    white-space: nowrap;
  }
  .headline__main {
    position: absolute;
    left: 100px;
    top: 769px;
    font-size: 126px;
    line-height: 1;
    font-weight: 800;
    letter-spacing: -1px;
    white-space: nowrap;
  }
  .services {
    position: absolute;
    left: 99px;
    top: 897px;
    margin: 0;
    padding: 0;
    list-style: none;
    display: flex;
    gap: 44px;
    font-weight: 500;
    font-size: 42px;
    line-height: 1;
    white-space: nowrap;
  }
  .services__item {
    display: flex;
    align-items: center;
    gap: 16px;
  }
  .services__tick { width: 29px; height: 25px; }
  .footer-band {
    position: absolute;
    left: 0;
    top: 1003px;
    width: 1200px;
    height: 197px;
    background: var(--brand-navy);
  }
  .footer-band__copy {
    position: absolute;
    left: 99px;
    top: 50px;
    margin: 0;
    font-weight: 500;
    font-size: 32px;
    line-height: 47px;
    white-space: nowrap;
  }
  .cta {
    position: absolute;
    left: 877px;
    top: 67px;
    width: 232px;
    height: 72px;
    background: var(--white);
    border-radius: 9px;
    display: flex;
    align-items: center;
    justify-content: center;
    gap: 12px;
    font-weight: 700;
    font-size: 32px;
    color: var(--sky);
    text-decoration: none;
  }
  .cta__arrow { width: 20px; height: 26px; }
</style>
</head>
<body>
<main class="ad">
  <svg class="ad__backdrop" viewBox="0 0 1200 1200" xmlns="http://www.w3.org/2000/svg">
    <defs>
      <linearGradient id="woodTone" x1="0" y1="0" x2="1" y2="1">
        <stop offset="0" stop-color="#4a3323"/>
        <stop offset="0.5" stop-color="#5e4130"/>
        <stop offset="1" stop-color="#3b2a1f"/>
      </linearGradient>
    </defs>
    <rect role="img" aria-label="Foto: Reinigungsutensilien auf Holzboden – Kehrschaufel, Farbroller, Sprühflasche, blaue Handschuhe und Schwamm" x="0" y="0" width="1200" height="1003" fill="url(#woodTone)"/>
    <polygon points="143,0 1200,0 1200,373 778,510" fill="#ffffff"/>
    <polygon points="0,765 1200,373 1200,1003 0,1003" fill="#4f8fd9" opacity="0.88"/>
    <polygon points="778,510 1200,373 1200,850" fill="#41b8a8" opacity="0.55"/>
  </svg>

  <div class="brand">
    <div class="brand__square"></div>
    <div class="brand__text">
      <span class="brand__name">Kolva<br>Putz</span>
      <span class="brand__owner">Inh. Tiago Ferrante</span>
    </div>
  </div>

  <h1 class="headline">
    <span class="headline__lead">Schenken Sie Ihrem Objekt</span>
    <span class="headline__main">Neuen Glanz</span>
  </h1>

  <ul class="services">
    <li class="services__item"><svg class="services__tick" viewBox="0 0 28 24"><path d="M3 13 L11 20 L25 4" fill="none" stroke="#fff" stroke-width="4.5" stroke-linecap="round" stroke-linejoin="round"/></svg>Büros</li>
    <li class="services__item"><svg class="services__tick" viewBox="0 0 28 24"><path d="M3 13 L11 20 L25 4" fill="none" stroke="#fff" stroke-width="4.5" stroke-linecap="round" stroke-linejoin="round"/></svg>Treppenhäuser</li>
    <li class="services__item"><svg class="services__tick" viewBox="0 0 28 24"><path d="M3 13 L11 20 L25 4" fill="none" stroke="#fff" stroke-width="4.5" stroke-linecap="round" stroke-linejoin="round"/></svg>Privathaushalte</li>
  </ul>

  <section class="footer-band">
    <p class="footer-band__copy">Zuverlässige, professionelle Reinigungskräfte<br>in den Kreisen Paderborn &amp; Gütersloh</p>
    <a class="cta" href="https://www.kolvaputz.de">Anfragen
      <svg class="cta__arrow" viewBox="0 0 20 26"><path d="M3 2 L16 13 L3 24" fill="none" stroke="#6db72e" stroke-width="6" stroke-linejoin="miter"/></svg>
    </a>
  </section>
</main>
</body>
</html>
```